Business card required for IT Consultancy Business - Bluefern Consulting.
Company provides the whole nine yards of services across IT Architecture, design and execution.
Basically we provide consulting services to help businesses make sure their technology is enabling their business strategy.
Design for front and back required.
We would like the front of the card to inlcude:
Name
Title
Mobile number
email address
www.BFQ.com.au
Company logos attached.
Thank you
Industry/Entity Type
Business
Contact Information for Business Card
Name
Title
Mobile number
email address
www.BFQ.com.au
Look and feel
Each slider illustrates characteristics of the customer's brand and the style your logo design should communicate.

```html
<!DOCTYPE html>
<html lang="en">
<head>
<meta charset="utf-8">
<title>Bluefern Consulting – Business Card</title>
<link rel="stylesheet" href="https://fonts.googleapis.com/css2?family=Montserrat:wght@400;500;600&display=swap">
<style>
  :root {
    --backdrop: #3b3b3d;
    --card: #161617;
    --card-edge: #0c0c0d;
    --blue: #1f7fd0;
    --orange: #f05a22;
    --white: #f2f2f2;
    --silver: #bdbdbd;
    --divider: #d8d8d8;
  }
  * { box-sizing: border-box; margin: 0; padding: 0; }
  html, body { width: 1200px; height: 864px; overflow: hidden; }
  body {
    background: var(--backdrop);
    font-family: "Montserrat", Arial, sans-serif;
    display: flex;
    flex-direction: column;
    align-items: center;
    justify-content: center;
    gap: 44px;
  }
  .card {
    width: 630px;
    height: 360px;
    background: var(--card);
    border-radius: 4px;
    box-shadow: 0 6px 0 var(--card-edge), 0 18px 40px rgba(0,0,0,.45);
    position: relative;
  }
  /* back */
  .card--back { display: flex; align-items: center; justify-content: center; }
  .back-mark {
    display: flex; align-items: center; gap: 14px;
    color: var(--silver); font-weight: 600; font-size: 30px; letter-spacing: .5px;
  }
  .back-mark .dot { width: 22px; height: 22px; border-radius: 50%; background: var(--silver); }
  /* front */
  .card--front {
    display: flex; align-items: center;
    padding: 0 48px 0 60px;
  }
  .brand {
    width: 270px;
    display: flex; align-items: center; gap: 12px;
    color: var(--blue); font-weight: 600; font-size: 25px; line-height: 1.1;
  }
  .brand .dot { flex: none; width: 20px; height: 20px; border-radius: 50%; background: var(--orange); }
  .divider { width: 2px; height: 124px; background: var(--divider); margin: 0 30px 0 20px; }
  .details { color: var(--white); }
  .person-name { color: var(--blue); font-weight: 600; font-size: 22px; }
  .person-title { font-size: 15px; margin-top: 2px; }
  .contact-list { list-style: none; margin-top: 26px; font-size: 15px; }
  .contact-list li { display: flex; align-items: center; gap: 9px; line-height: 22px; }
  .contact-list svg { width: 13px; height: 13px; flex: none; }
</style>
</head>
<body>
  <section class="card card--back" aria-label="Card back">
    <div class="back-mark"><span class="dot"></span>Bluefern</div>
  </section>

  <section class="card card--front" aria-label="Card front">
    <div class="brand"><span class="dot"></span><span>Bluefern Consulting</span></div>
    <div class="divider"></div>
    <div class="details">
      <p class="person-name">Daniel Reeve</p>
      <p class="person-title">President</p>
      <ul class="contact-list">
        <li>
          <svg viewBox="0 0 12 12" fill="none" stroke="var(--orange)" stroke-width="1.4"><rect x="3" y="1" width="6" height="10" rx="1"/><line x1="5" y1="9.2" x2="7" y2="9.2"/></svg>
          012-555-0148
        </li>
        <li>
          <svg viewBox="0 0 12 12" fill="none" stroke="var(--orange)" stroke-width="1.4"><rect x="1" y="2.5" width="10" height="7"/><polyline points="1,2.5 6,7 11,2.5"/></svg>
          info@BFQ.com.au
        </li>
        <li>
          <svg viewBox="0 0 12 12" fill="none" stroke="var(--orange)" stroke-width="1.2"><circle cx="6" cy="6" r="5"/><ellipse cx="6" cy="6" rx="2.2" ry="5"/><line x1="1" y1="6" x2="11" y2="6"/></svg>
          www.BFQ.com.au
        </li>
      </ul>
    </div>
  </section>
</body>
</html>
```